Velmora and Co Business Card Design

Looking for a business card design. Wanting Smart, Clean and Sharp looking to promote Velmora and Co, our Import Export Business - like Black, White and natural textures. I have uploaded our logo. I like a rounded font but open to other ideas
Being that we have a wide range of products on offer we are looking for a neutral yet eye catching card. We would also like to have Import - Export on the business card to be clear on want our business does.

Target Market(s)

Import export market

Industry/Entity Type

Importer

Contact Information for Business Card

Mr Tobias Kernwell
tobias.kernwell@velmoraandco.com.au
+61 (0) 417 630 284
www.velmoraandco.com.au

Font styles to use
Other font styles liked:
• Unsure of actual font name but something rounded and clean

Colors

Designer to choose colors to be used in the design.

Requirements
Must have
• Snapverse icon
• Friendwall icon

```html
<!DOCTYPE html>
<html lang="en">
<head>
<meta charset="utf-8">
<title>Velmora and Co Business Card</title>
<link rel="stylesheet" href="https://fonts.googleapis.com/css2?family=Oswald:wght@500;700&family=Open+Sans:wght@400;600&display=swap">
<style>
  :root {
    --page: #e9e7e4;
    --card-white: #ffffff;
    --card-black: #1f1f1f;
    --ink: #1a1a1a;
    --ink-soft: #333333;
    --logo-fill: #3a3a3a;
    --on-dark: #f2f2f2;
    --on-dark-soft: #a9a9a9;
  }
  * { box-sizing: border-box; margin: 0; padding: 0; }
  html, body { width: 1200px; height: 900px; overflow: hidden; background: var(--page); }
  .canvas { position: relative; width: 1200px; height: 900px; }

  .card {
    position: absolute;
    left: 280px;
    width: 640px;
    height: 366px;
    box-shadow: 0 6px 18px rgba(0,0,0,0.18);
  }
  .card--back { top: 60px; background: var(--card-black); }
  .card--front { top: 474px; background: var(--card-white); }

  /* Back */
  .back-mark {
    position: absolute; left: 50%; top: 50%;
    transform: translate(-50%, -56%);
    display: flex; align-items: center; gap: 16px;
  }
  .back-mark__square { width: 34px; height: 34px; border: 4px solid var(--on-dark); }
  .back-mark__name {
    font-family: "Oswald", sans-serif; font-weight: 700;
    font-size: 40px; letter-spacing: 1px; color: var(--on-dark); text-transform: uppercase;
  }
  .back-url {
    position: absolute; right: 40px; bottom: 32px;
    font-family: "Open Sans", sans-serif; font-size: 13px;
    letter-spacing: 4px; color: var(--on-dark-soft);
  }

  /* Front */
  .identity { position: absolute; left: 46px; top: 40px; }
  .identity__name {
    font-family: "Oswald", sans-serif; font-weight: 700;
    font-size: 34px; line-height: 1; color: var(--ink); letter-spacing: -0.5px;
  }
  .identity__title {
    font-family: "Open Sans", sans-serif; font-size: 14px;
    letter-spacing: 1px; color: var(--ink-soft); margin-top: 4px;
  }
  .identity__rule { width: 42px; height: 3px; background: var(--ink); margin-top: 22px; }

  .brand {
    position: absolute; right: 40px; top: 48px;
    display: flex; align-items: center; gap: 10px;
  }
  .brand__square { width: 26px; height: 26px; background: var(--logo-fill); }
  .brand__name {
    font-family: "Oswald", sans-serif; font-weight: 700;
    font-size: 26px; color: var(--logo-fill); text-transform: uppercase;
  }

  .contact { position: absolute; left: 46px; bottom: 40px; list-style: none; }
  .contact__item {
    display: flex; align-items: center; gap: 10px;
    font-family: "Open Sans", sans-serif; font-size: 15px; color: var(--ink);
    line-height: 26px;
  }
  .contact__icon { width: 14px; height: 14px; flex: none; }

  .social { position: absolute; right: 40px; bottom: 40px; list-style: none; }
  .social__item {
    display: flex; align-items: center; justify-content: flex-end; gap: 10px;
    font-family: "Open Sans", sans-serif; font-size: 15px; color: var(--ink-soft);
    line-height: 28px;
  }
  .social__square { width: 14px; height: 14px; background: var(--ink-soft); }
</style>
</head>
<body>
<main class="canvas">

  <section class="card card--back" aria-label="Card back">
    <div class="back-mark">
      <span class="back-mark__square"></span>
      <span class="back-mark__name">Velmora &amp; Co</span>
    </div>
    <p class="back-url">www.velmoraandco.com.au</p>
  </section>

  <section class="card card--front" aria-label="Card front">
    <div class="identity">
      <h1 class="identity__name">YOUR NAME</h1>
      <p class="identity__title">JOB TITLE</p>
      <div class="identity__rule"></div>
    </div>

    <div class="brand">
      <span class="brand__square"></span>
      <span class="brand__name">Velmora &amp; Co</span>
    </div>

    <ul class="contact">
      <li class="contact__item">
        <svg class="contact__icon" viewBox="0 0 14 14" aria-hidden="true">
          <rect x="0.5" y="2.5" width="13" height="9" fill="#1a1a1a"/>
          <path d="M0.5 2.5 L7 8 L13.5 2.5" fill="none" stroke="#ffffff" stroke-width="1.2"/>
        </svg>
        tobias.kernwell@velmoraandco.com.au
      </li>
      <li class="contact__item">
        <svg class="contact__icon" viewBox="0 0 14 14" aria-hidden="true">
          <path d="M4 1 L6 4 L4.5 5.5 C5.3 7.5 6.5 8.7 8.5 9.5 L10 8 L13 10 L11.5 12.8 C6 12.5 1.5 8 1.2 2.5 Z" fill="#1a1a1a"/>
        </svg>
        +61 (0) 417 630 284
      </li>
      <li class="contact__item">
        <svg class="contact__icon" viewBox="0 0 14 14" aria-hidden="true">
          <g fill="none" stroke="#1a1a1a" stroke-width="1.1">
            <circle cx="7" cy="7" r="6"/>
            <ellipse cx="7" cy="7" rx="2.6" ry="6"/>
            <line x1="1" y1="7" x2="13" y2="7"/>
            <line x1="2" y1="4" x2="12" y2="4"/>
            <line x1="2" y1="10" x2="12" y2="10"/>
          </g>
        </svg>
        www.velmoraandco.com.au
      </li>
    </ul>

    <ul class="social">
      <li class="social__item">snapverse link/ <span class="social__square"></span></li>
      <li class="social__item">friendwall link/ <span class="social__square"></span></li>
    </ul>
  </section>

</main>
</body>
</html>
```